Bright Ledger Path's Mortgage Arc

For BrightLedgerPath.org - Creating a sequence of web pages for consumers to understand their mortgage through Mortgage Arc. There are six pages - want the designer to be willing to design and code those six pages. Most of the pages are very similar.

```html
<!DOCTYPE html>
<html lang="en">
<head>
<meta charset="UTF-8">
<title>Mortgage Central – Bright Ledger Path</title>
<link href="https://fonts.googleapis.com/css2?family=Poppins:wght@500;600;700&display=swap" rel="stylesheet">
<style>
  :root {
    --page-bg: #f8f8f8;
    --brand-blue: #2b5ed1;
    --brand-navy: #1f4fbf;
    --brand-green: #17a84c;
    --brand-teal: #1a8a86;
    --tile-text: #ffffff;
    --banner-text: #ffffff;
  }
  * { box-sizing: border-box; margin: 0; padding: 0; }
  html, body {
    width: 1200px;
    height: 717px;
    overflow: hidden;
    background: var(--page-bg);
    font-family: "Poppins", sans-serif;
  }
  .page {
    position: relative;
    width: 1200px;
    height: 717px;
  }
  .site-header {
    position: absolute;
    left: 88px;
    top: 28px;
    height: 42px;
    display: flex;
    align-items: center;
    gap: 9px;
  }
  .brand-mark {
    width: 30px;
    height: 30px;
    border-radius: 4px;
    background: var(--brand-navy);
  }
  .brand-name {
    font-size: 17.5px;
    font-weight: 500;
    color: var(--brand-navy);
    letter-spacing: -0.1px;
  }
  .section-banner {
    position: absolute;
    left: 0;
    top: 99px;
    width: 1200px;
    height: 88px;
    background: linear-gradient(90deg, var(--brand-navy) 0%, #2a6ab8 35%, var(--brand-teal) 65%, var(--brand-green) 100%);
    display: flex;
    align-items: center;
  }
  .banner-title {
    margin-left: 83px;
    font-size: 26px;
    font-weight: 600;
    color: var(--banner-text);
    letter-spacing: 0.2px;
  }
  .tile-grid {
    position: absolute;
    left: 85px;
    top: 226px;
    display: grid;
    grid-template-columns: repeat(4, 246px);
    grid-template-rows: repeat(2, 219px);
    column-gap: 16px;
    row-gap: 14px;
  }
  .nav-tile {
    background: var(--brand-blue);
    border-radius: 11px;
    display: flex;
    align-items: center;
    justify-content: center;
    text-align: center;
    color: var(--tile-text);
    font-size: 21px;
    font-weight: 700;
    line-height: 28px;
    text-transform: uppercase;
    text-decoration: none;
  }
</style>
</head>
<body>
  <main class="page">
    <header class="site-header">
      <span class="brand-mark"></span>
      <span class="brand-name">BrightLedgerPath</span>
    </header>

    <section class="section-banner" role="img" aria-label="Banner photo of a hand using a laptop with financial charts, tinted blue to green">
      <h1 class="banner-title">Mortgage Central</h1>
    </section>

    <nav class="tile-grid">
      <a class="nav-tile" href="#">Edit<br>Mortgage<br>Profile</a>
      <a class="nav-tile" href="#">Maximum<br>Mortgage<br>Qualification</a>
      <a class="nav-tile" href="#">Specific<br>Mortgage<br>Amount</a>
      <a class="nav-tile" href="#">Specific<br>Mortgage<br>Payment</a>
      <a class="nav-tile" href="#">Conventional<br>Mortgage<br>Options</a>
      <a class="nav-tile" href="#">FHA<br>Mortgage<br>Options</a>
      <a class="nav-tile" href="#">VA<br>Mortgage<br>Options</a>
      <a class="nav-tile" href="#">USDA<br>Mortgage<br>Options</a>
    </nav>
  </main>
</body>
</html>
```